We need a Chatterbox ad design for mobile app business.

"LUMAVO" app platform providing a range of services like home massage therapy or home hair cut needs 4 Chatterbox advertisement designs to hire the service providers. Each ad needs to bold one the professions and also show the others professions!! let say we we need one design emphasizing on Massage Therapist, one for hair stylists, one for tune up technicians, and that includes 4 professions : house keepers + lawn mowers, snow blowers and tutors. Each one of the designs requires a different content.
This app is gonna lunch in Thunder Bay/ON/Canada, So it is necessary to be mentioned. And even a design must be included the pandemic situation for some professions and EARNING A SIDE INCOME UP TO 50K PER YEAR AND ALSO TO BE YOUR OWN BOSS!.
Lumavo is service application that provides different ranges of services like automotive service, home cleaning, massage therapy and etc. So the design must be a very nice combination of services and very clear.

To get better understanding of the app please check it in the quindel market store or brisk store through following links:
https://apps.quindelmarket.example/details?id=com.lumavojobs

Requirements
Nice to have
• Apply green, silver and golden colors

```html
<!DOCTYPE html>
<html lang="en">
<head>
<meta charset="utf-8">
<title>Lumavo – Service Provider Ads</title>
<link rel="stylesheet" href="https://fonts.googleapis.com/css2?family=Montserrat:wght@300;400;600;700;800;900&display=swap">
<style>
  :root {
    --green: #13c13a;
    --green-deep: #0d7a24;
    --green-dark: #0a5e1b;
    --gold: #c9a24a;
    --gold-light: #e8cf8a;
    --gold-dark: #9c7a2c;
    --black: #000;
    --white: #fff;
    --bg: #ececec;
  }
  * { margin: 0; padding: 0; box-sizing: border-box; }
  html, body { width: 1200px; height: 1200px; overflow: hidden; }
  body { background: var(--bg); position: relative; font-family: "Montserrat", sans-serif; }

  .ad {
    position: absolute;
    width: 765px; height: 765px;
    transform: scale(0.6211);
    transform-origin: top left;
    background: var(--white);
    overflow: hidden;
  }
  .ad--massage { left: 396px; top: 75px; }
  .ad--hair    { left: 102px; top: 619px; }
  .ad--tuneup  { left: 671px; top: 619px; }

  .ad__art { position: absolute; inset: 0; }

  .brand { position: absolute; left: 55px; top: 55px; width: 200px; text-align: center; }
  .brand__dot {
    width: 84px; height: 84px; margin: 0 auto 14px;
    border-radius: 50%; border: 9px solid var(--green);
  }
  .brand__name { font-weight: 800; font-size: 42px; color: var(--green); letter-spacing: 1px; }

  .headline { position: absolute; left: 38px; color: var(--white); white-space: nowrap; }
  .headline__kicker { font-weight: 300; font-size: 36px; letter-spacing: 6px; color: var(--black); line-height: 1; }
  .headline__role { font-weight: 900; line-height: 0.92; letter-spacing: -1px; }

  .ad--massage .headline { top: 432px; }
  .ad--massage .headline__role--a { font-size: 70px; margin-top: 4px; }
  .ad--massage .headline__role--b { font-size: 62px; margin-top: 2px; }

  .ad--hair .headline { top: 415px; left: 60px; }
  .ad--hair .headline__kicker { font-size: 31px; letter-spacing: 5px; }
  .ad--hair .headline__role--a { font-size: 120px; margin-top: 0; line-height: 0.82; }
  .ad--hair .headline__role--b { font-size: 68px; line-height: 0.95; }

  .ad--tuneup .headline { top: 452px; left: 42px; }
  .ad--tuneup .headline__kicker { font-size: 34px; letter-spacing: 6px; }
  .ad--tuneup .headline__role--a { font-size: 75px; margin-top: 2px; }
  .ad--tuneup .headline__role--b { font-size: 48px; }

  .home-pill {
    position: absolute; left: 27px; top: 597px; width: 398px; height: 52px;
    border-radius: 26px;
    background: linear-gradient(180deg, var(--gold-light), var(--gold) 55%, var(--gold-dark));
    font-weight: 800; font-size: 44px; color: var(--black);
    display: flex; align-items: center; justify-content: center; line-height: 1;
  }
  .ad--hair .home-pill, .ad--tuneup .home-pill { left: 42px; top: 611px; width: 368px; font-size: 41px; }

  .book-btn {
    position: absolute; left: 132px; top: 673px; width: 186px; height: 38px;
    border-radius: 19px; background: var(--black); border: 3px solid var(--gold);
    color: var(--white); font-weight: 800; font-size: 23px; letter-spacing: 1px;
    display: flex; align-items: center; justify-content: center;
  }

  .footer-bar {
    position: absolute; left: 0; right: 0; bottom: 0; height: 70px;
    background: var(--black); border-top: 6px solid var(--gold);
  }
  .footer-bar__text { position: absolute; left: 55px; top: 24px; color: var(--white); font-size: 16px; letter-spacing: .4px; }
  .store-badge { position: absolute; top: 20px; height: 26px; border-radius: 4px; border: 1px solid #777; background: #111; }
  .store-badge--brisk { left: 258px; width: 66px; }
  .store-badge--quindel { left: 340px; width: 78px; }

  .launch {
    position: absolute; left: 450px; top: 508px; width: 280px;
    text-align: center; color: var(--white); font-weight: 700; font-size: 20px; line-height: 1.25;
  }
  .earn-box {
    position: absolute; left: 496px; top: 598px; width: 197px; height: 167px;
    border-radius: 12px 12px 0 0;
    background: linear-gradient(180deg, var(--gold-light), var(--gold) 45%, var(--gold-dark));
    color: #111; font-weight: 800; font-size: 16.5px; line-height: 1.28;
    text-align: center; padding-top: 20px;
  }
</style>
</head>
<body>

<section class="ad ad--massage">
  <svg class="ad__art" viewBox="0 0 765 765" width="765" height="765">
    <defs>
      <linearGradient id="bandA" x1="0" y1="0" x2="0" y2="1">
        <stop offset="0" stop-color="#16c43c"/><stop offset=".55" stop-color="#0f8f2a"/><stop offset="1" stop-color="#0a5e1b"/>
      </linearGradient>
      <linearGradient id="photoA" x1="0" y1="0" x2="1" y2="1">
        <stop offset="0" stop-color="#f3f0ee"/><stop offset=".55" stop-color="#8a5a3e"/><stop offset="1" stop-color="#ece7ea"/>
      </linearGradient>
    </defs>
    <rect x="0" y="385" width="765" height="14" fill="var(--gold)"/>
    <rect x="0" y="399" width="765" height="300" fill="url(#bandA)"/>
    <circle cx="567" cy="215" r="278" fill="var(--gold)"/>
    <circle cx="567" cy="215" r="270" fill="var(--green)"/>
    <circle cx="567" cy="215" r="236" fill="var(--gold)"/>
    <circle cx="567" cy="215" r="230" fill="url(#photoA)" role="img" aria-label="Photo of a massage therapist working on a client's back"/>
    <rect x="265" y="300" width="92" height="30" rx="15" fill="var(--green)" stroke="var(--gold)" stroke-width="5"/>
    <rect x="119" y="350" width="140" height="30" rx="15" fill="var(--green)" stroke="var(--gold)" stroke-width="5"/>
    <rect x="295" y="355" width="70" height="28" rx="14" fill="var(--green)" stroke="var(--gold)" stroke-width="5"/>
  </svg>
  <div class="brand"><div class="brand__dot"></div><div class="brand__name">LUMAVO</div></div>
  <div class="headline">
    <div class="headline__kicker">PROFESSIONAL</div>
    <div class="headline__role headline__role--a">MASSAGE</div>
    <div class="headline__role headline__role--b">THERAPIST</div>
  </div>
  <div class="home-pill">AT YOUR HOME</div>
  <div class="launch">This app is gonna<br>lunch in<br>Thunder Bay/ON/Canada</div>
  <div class="footer-bar">
    <span class="footer-bar__text">Download the app now</span>
    <span class="store-badge store-badge--brisk"></span>
    <span class="store-badge store-badge--quindel"></span>
  </div>
  <div class="book-btn">BOOK NOW</div>
  <div class="earn-box">EARNING A SIDE<br>INCOME UP TO<br>50K PER YEAR<br>AND ALSO TO<br>BE YOUR OWN<br>BOSS!</div>
</section>

<section class="ad ad--hair">
  <svg class="ad__art" viewBox="0 0 765 765" width="765" height="765">
    <defs>
      <linearGradient id="bandB" x1="0" y1="0" x2="0" y2="1">
        <stop offset="0" stop-color="#16c43c"/><stop offset=".55" stop-color="#0f8f2a"/><stop offset="1" stop-color="#0a5e1b"/>
      </linearGradient>
      <linearGradient id="photoB" x1="0" y1="0" x2="1" y2="1">
        <stop offset="0" stop-color="#5d5a58"/><stop offset=".5" stop-color="#3a2e2a"/><stop offset="1" stop-color="#8c8682"/>
      </linearGradient>
    </defs>
    <rect x="0" y="385" width="765" height="14" fill="var(--gold)"/>
    <rect x="0" y="399" width="765" height="300" fill="url(#bandB)"/>
    <circle cx="567" cy="215" r="278" fill="var(--gold)"/>
    <circle cx="567" cy="215" r="270" fill="var(--green)"/>
    <circle cx="567" cy="215" r="236" fill="var(--gold)"/>
    <circle cx="567" cy="215" r="230" fill="url(#photoB)" role="img" aria-label="Photo of a barber styling a client's hair with a brush and clippers"/>
    <rect x="265" y="300" width="92" height="30" rx="15" fill="var(--green)" stroke="var(--gold)" stroke-width="5"/>
    <rect x="119" y="350" width="140" height="30" rx="15" fill="var(--green)" stroke="var(--gold)" stroke-width="5"/>
    <rect x="295" y="355" width="70" height="28" rx="14" fill="var(--green)" stroke="var(--gold)" stroke-width="5"/>
  </svg>
  <div class="brand"><div class="brand__dot"></div><div class="brand__name">LUMAVO</div></div>
  <div class="headline">
    <div class="headline__kicker">PROFESSIONAL</div>
    <div class="headline__role headline__role--a">HAIR</div>
    <div class="headline__role headline__role--b">STYLISTS</div>
  </div>
  <div class="home-pill">AT YOUR HOME</div>
  <div class="launch">This app is gonna<br>lunch in<br>Thunder Bay/ON/Canada</div>
  <div class="footer-bar">
    <span class="footer-bar__text">Download the app now</span>
    <span class="store-badge store-badge--brisk"></span>
    <span class="store-badge store-badge--quindel"></span>
  </div>
  <div class="book-btn">BOOK NOW</div>
  <div class="earn-box">EARNING A SIDE<br>INCOME UP TO<br>50K PER YEAR<br>AND ALSO TO<br>BE YOUR OWN<br>BOSS!</div>
</section>

<section class="ad ad--tuneup">
  <svg class="ad__art" viewBox="0 0 765 765" width="765" height="765">
    <defs>
      <linearGradient id="bandC" x1="0" y1="0" x2="0" y2="1">
        <stop offset="0" stop-color="#16c43c"/><stop offset=".55" stop-color="#0f8f2a"/><stop offset="1" stop-color="#0a5e1b"/>
      </linearGradient>
      <linearGradient id="photoC" x1="0" y1="0" x2="1" y2="1">
        <stop offset="0" stop-color="#3f4246"/><stop offset=".5" stop-color="#6c7078"/><stop offset="1" stop-color="#d6d4cf"/>
      </linearGradient>
    </defs>
    <rect x="0" y="385" width="765" height="14" fill="var(--gold)"/>
    <rect x="0" y="399" width="765" height="300" fill="url(#bandC)"/>
    <circle cx="567" cy="215" r="278" fill="var(--gold)"/>
    <circle cx="567" cy="215" r="270" fill="var(--green)"/>
    <circle cx="567" cy="215" r="236" fill="var(--gold)"/>
    <circle cx="567" cy="215" r="230" fill="url(#photoC)" role="img" aria-label="Photo of a mechanic inspecting a car engine in a workshop"/>
    <rect x="265" y="300" width="92" height="30" rx="15" fill="var(--green)" stroke="var(--gold)" stroke-width="5"/>
    <rect x="119" y="350" width="140" height="30" rx="15" fill="var(--green)" stroke="var(--gold)" stroke-width="5"/>
    <rect x="295" y="355" width="70" height="28" rx="14" fill="var(--green)" stroke="var(--gold)" stroke-width="5"/>
  </svg>
  <div class="brand"><div class="brand__dot"></div><div class="brand__name">LUMAVO</div></div>
  <div class="headline">
    <div class="headline__kicker">PROFESSIONAL</div>
    <div class="headline__role headline__role--a">TUNE UP</div>
    <div class="headline__role headline__role--b">TECHNICIANS</div>
  </div>
  <div class="home-pill">AT YOUR HOME</div>
  <div class="launch">This app is gonna<br>lunch in<br>Thunder Bay/ON/Canada</div>
  <div class="footer-bar">
    <span class="footer-bar__text">Download the app now</span>
    <span class="store-badge store-badge--brisk"></span>
    <span class="store-badge store-badge--quindel"></span>
  </div>
  <div class="book-btn">BOOK NOW</div>
  <div class="earn-box">EARNING A SIDE<br>INCOME UP TO<br>50K PER YEAR<br>AND ALSO TO<br>BE YOUR OWN<br>BOSS!</div>
</section>

</body>
</html>
```